Restaurant needs a vertical banner for fried catfish

Our restaurant is looking for an eye-catching 78.75in. x 36in. vertical physical banner ad for our fried catfish. Photos for the fried catfish will be provided as a reference but we will also accept anything similar to the photo. We will be using the following as our receptacle: https://www.plankoria.example/banner-stand/retractable-banner-stands/
The design must incorporate the following flavor texts:
Fried Catfish
Always Fresh!
Made from Scratch
Hand-cut Fillets
The Best Catfish in Texas
Served with fries, hush puppies, and a 32oz fountain drink
Also available by the pound!
The final design should be creative, professional, and eye-catching for customers.
Updates
Colors
Designer to choose colors to be used in the design.
Requirements
Must have
- We are open to any and all design elements, albeit the 'flavor texts' should not overpower, but complement the fried catfish photo. 'Fried Catfish' can be used in lieu of a main title/logo.
Nice to have
- Transparent or textured backgrounds that can encompass any or all part of the banner such as a cutting board, shadows, abstract, etc to show depth are a plus.
- Use of vectors or objects such as ribbons or shapes to encapsulate the 'flavor texts' are also encouraged.

```html
<!DOCTYPE html>
<html lang="en">
<head>
<meta charset="utf-8">
<title>Fried Catfish Banner</title>
<link rel="stylesheet" href="https://fonts.googleapis.com/css2?family=Yellowtail&family=Kaushan+Script&family=Roboto+Condensed:ital,wght@0,500;1,300&display=block">
<style>
  :root {
    --stage: #777777;
    --gold-light: #F0C66B;
    --gold-mid: #E8B550;
    --gold-deep: #E2AA3F;
    --gold-bar: #DFA73A;
    --gold-shadow: #B88A2C;
    --blue-mid: #1E5C87;
    --blue-deep: #06486D;
    --blue-dark: #0B3450;
    --white: #FFFFFF;
    --ink: #1A1A1A;
    --bullet: #E8B550;
  }
  html, body {
    margin: 0;
    width: 1200px;
    height: 1200px;
    overflow: hidden;
    background: var(--stage);
  }
  .banner {
    position: absolute;
    left: 339px;
    top: 28px;
    width: 523px;
    height: 1143px;
    overflow: hidden;
    background: var(--gold-light);
  }
  .banner-waves {
    position: absolute;
    inset: 0;
  }
  .brand-mark {
    position: absolute;
    display: flex;
    align-items: center;
    justify-content: center;
    background: var(--white);
    border-radius: 50%;
    font-family: "Roboto Condensed", sans-serif;
    font-weight: 500;
    color: var(--ink);
    z-index: 3;
  }
  .brand-mark--top {
    left: 190px;
    top: 36px;
    width: 146px;
    height: 130px;
    font-size: 44px;
  }
  .brand-mark--bottom {
    left: 232px;
    top: 1076px;
    width: 58px;
    height: 58px;
    font-size: 16px;
  }
  .title {
    position: absolute;
    margin: 0;
    font-family: "Yellowtail", "Kaushan Script", cursive;
    font-weight: 400;
    color: var(--white);
    text-shadow: 4px 4px 0 var(--gold-shadow);
    line-height: 1;
    white-space: nowrap;
    transform-origin: center center;
    transform: translate(-50%, -50%) rotate(-12deg);
    z-index: 2;
  }
  .title--fried { left: 215px; top: 285px; font-size: 150px; }
  .title--catfish { left: 290px; top: 398px; font-size: 150px; }
  .hero-photo {
    position: absolute;
    left: -20px;
    top: 468px;
    width: 580px;
    height: 312px;
    border-radius: 50% / 48%;
    background: radial-gradient(ellipse at 55% 40%, #C07A2E 0%, #A8692A 35%, #D8B36A 60%, #F2EEE6 78%, #E9E6E0 100%);
    z-index: 1;
  }
  .thumb {
    position: absolute;
    box-sizing: border-box;
    border: 5px solid var(--white);
    background: linear-gradient(180deg, #C9463A 0%, #D9A23A 30%, #B9772E 55%, #A0652A 100%);
    z-index: 2;
  }
  .thumb--one { left: 333px; top: 720px; width: 152px; height: 106px; transform: rotate(-6deg); }
  .thumb--two { left: 325px; top: 832px; width: 148px; height: 106px; }
  .thumb--three { left: 340px; top: 950px; width: 146px; height: 106px; transform: rotate(-3deg); }
  .features {
    position: absolute;
    left: 34px;
    top: 812px;
    margin: 0;
    padding: 0;
    list-style: none;
    font-family: "Roboto Condensed", sans-serif;
    font-style: italic;
    font-weight: 300;
    font-size: 22px;
    line-height: 32.3px;
    letter-spacing: -0.3px;
    color: var(--white);
    z-index: 2;
  }
  .features li {
    position: relative;
    padding-left: 21px;
    width: 300px;
    white-space: nowrap;
  }
  .features li::before {
    content: "";
    position: absolute;
    left: 0;
    top: 11px;
    width: 11px;
    height: 11px;
    background: var(--bullet);
  }
</style>
</head>
<body>
  <main class="banner">
    <svg class="banner-waves" viewBox="0 0 523 1143" width="523" height="1143" aria-hidden="true">
      <path d="M0 184 C90 170 150 205 230 200 C320 190 380 170 523 220 L523 1143 L0 1143 Z" fill="var(--gold-mid)"/>
      <path d="M0 440 C120 420 260 470 523 380 L523 1143 L0 1143 Z" fill="var(--gold-deep)"/>
      <path d="M0 720 C150 700 330 660 523 690 L523 1143 L0 1143 Z" fill="var(--blue-mid)"/>
      <path d="M0 820 C120 790 260 880 380 880 C450 880 490 860 523 855 L523 1143 L0 1143 Z" fill="var(--blue-deep)"/>
      <path d="M0 1065 C150 1040 300 1080 523 1030 L523 1143 L0 1143 Z" fill="var(--blue-dark)"/>
      <rect x="0" y="1093" width="523" height="50" fill="var(--gold-bar)"/>
    </svg>

    <div class="brand-mark brand-mark--top">LOGO</div>

    <div class="hero-photo" role="img" aria-label="Photo of a plate of golden fried catfish fillets with fries, hush puppies and tartar sauce"></div>

    <h1 class="title title--fried">Fried</h1>
    <h1 class="title title--catfish">Catfish</h1>

    <div class="thumb thumb--one" role="img" aria-label="Photo of fried catfish fillets with tomatoes, lemons and onion"></div>
    <div class="thumb thumb--two" role="img" aria-label="Photo of a catfish plate with fries and hush puppies"></div>
    <div class="thumb thumb--three" role="img" aria-label="Photo of catfish fillets with lemons, tomatoes and tartar sauce"></div>

    <ul class="features">
      <li>Always Fresh!</li>
      <li>Made from Scratch</li>
      <li>Hand-cut Fillets</li>
      <li>The Best Catfish in Texas</li>
      <li>Served with fries, hush puppies,<br>and a 32oz fountain drink</li>
      <li>Also available by the pound!</li>
    </ul>

    <div class="brand-mark brand-mark--bottom">LOGO</div>
  </main>
</body>
</html>
```